Diverse business needs a corporate identity system

Varrow Brisk Holdings Limited is a well established family owned and run business operating in Port Moresby, Papua New Guinea since 1989. As part of taking the business to the next level, we are redoing our branding/corporate identity.

We currently carry out two core business activities servicing corporate clients in the commercial and industrial sectors:
1. Electrical - new installations and maintenance work
2. Construction - mostly commercial & industrial, some residential

We are looking to add the following business activities in near future:
1. IT consulting
2. Property development - business/industrial park, residential complexes, low cost housing
3. Retail of hardware, construction supplies and flat pack furniture & kitchens

We have just completed our logo design here on SketchHarbor and now wanting to design business card and stationery based on our new logo (attached).

Deliverables are:
1. Business card - double sided
2. Letterhead A4

Details to go on the card:
Name: Martin Fenwale
Title: Director
Email: martin.fenwale@varrowbrisk.example
Tel: +675 3481720, +675 3487043
Office: Section 17 Lot 43, Kessaby Light Industrial Area, Port Moresby, Papua New Guinea
Postal: PO Box 914, Kessaby, NCD, Papua New Guinea
Website: varrowbrisk.example

Our services can be listed somewhere on the card:
Electrical, Construction, Property Development, IT Consulting

Details to go on the letterhead:
Varrow Brisk Holdings Ltd.
PO Box 914, Kessaby, NCD, Papua New Guinea
Fax: +675 3486158
Email: info@varrowbrisk.example

For inspiration, I have uploaded some images of business cards we like.

Would be good if the same/similar business card design could be printed both economically (e.g. full coloured both sides, matte card stock) for majority of staff and upscaled to use premium features such as letter pressed, foil etc for use by executives. Otherwise, please provide two separate designs.

Logo text font is nexa bold freefont - please use something from nexa family or another font type that complements it.

Reason: Few designs were submitted. Most were clearly from ready to use templates. No designs really stand out for us at the moment. So we have decided to narrow the focus to just business card and A4 letterhead. And also revised the brief to be completely open to hopefully invite more creative designs.

I have updated the brief to be a lot less restrictive to try and get more creative designs. Also uploaded more images of premium business cards for inspiration.

Construction

Requirements
Must have
• All designs must conform to quillpress specifications. Refer to and download appropriate work file templates from http://www.quillpress.example/uploads/templates.aspx?ref=5820146631&tab=0.
Should not have
• No QR codes and social media links.

```html
<!DOCTYPE html>
<html lang="en">
<head>
<meta charset="utf-8">
<title>VarrowBrisk Letterhead</title>
<link href="https://fonts.googleapis.com/css2?family=Exo:wght@400;600;700&family=Great+Vibes&display=swap" rel="stylesheet">
<style>
  :root {
    --backdrop: #e9e6df;
    --paper: #ffffff;
    --ink: #2b2b2b;
    --ink-soft: #6a6a6a;
    --brand-red: #e2332c;
    --brand-gold: #e9a21b;
  }
  * { margin: 0; padding: 0; box-sizing: border-box; }
  html, body {
    width: 1200px; height: 1000px; overflow: hidden;
    background: var(--backdrop);
    font-family: "Exo", sans-serif;
    color: var(--ink);
  }
  .letterhead {
    position: absolute;
    left: 270px; top: 33px;
    width: 660px; height: 934px;
    background: var(--paper);
    box-shadow: 0 4px 18px rgba(0,0,0,0.12);
    padding: 62px 58px 0 48px;
  }
  .brand {
    display: flex; align-items: center; gap: 10px;
  }
  .brand-dot {
    width: 26px; height: 26px; border-radius: 50%;
    background: var(--brand-gold);
  }
  .brand-name {
    font-size: 27px; font-weight: 600; color: var(--brand-red);
    letter-spacing: 0.2px;
  }
  .company {
    margin-top: 78px;
    font-size: 10.5px; line-height: 1.35; color: var(--ink-soft);
  }
  .company-name {
    font-size: 14.5px; font-weight: 700; color: var(--ink);
    margin-bottom: 2px;
  }
  .company p + p { margin-top: 10px; }
  .content {
    display: grid;
    grid-template-columns: 170px 1fr;
    margin-top: 40px;
  }
  .sender { font-size: 12px; line-height: 1.3; }
  .sender-role { color: var(--brand-red); }
  .letter { font-size: 12.2px; line-height: 1.45; }
  .letter p { margin-bottom: 14px; }
  .letter .body-text { text-align: justify; }
  .closing { margin-top: 20px; }
  .signature {
    font-family: "Great Vibes", cursive;
    font-size: 30px; color: var(--ink);
    margin-top: 12px;
  }
</style>
</head>
<body>
  <article class="letterhead">
    <header class="brand">
      <span class="brand-dot"></span>
      <span class="brand-name">VarrowBrisk</span>
    </header>

    <section class="company">
      <div class="company-name">VarrowBrisk</div>
      <p>12345 Your Street Adress,<br>YourTown, Your State,<br>Country, Zip 90210</p>
      <p>Phone : 012 345 6789<br>Fax : 012 345 6789<br>Mobile : 012 345 6789</p>
      <p>Email : mail@varrowbrisk.example<br>www.varrowbrisk.example</p>
    </section>

    <section class="content">
      <div class="sender">
        <div class="sender-name">Your Name</div>
        <div class="sender-role">Founder</div>
      </div>
      <div class="letter">
        <p>Dear sir,</p>
        <p>Even though using “lorem ipsum” often arouses curiosity due to its resemblance to classical Latin, it is not intended to have meaning. Where text is visible in a document, people tend to focus on the textual content rather than upon overall presentation, so publishers use lorem ipsum when displaying a typeface or design in order to direct the focus to presentation. “Lorem ipsum” also approximates a typical distribution of spaces in English.</p>
        <p class="body-text">The most common lorem ipsum text reads as follows: Lorem ipsum dolor sit amet, consectetur adipisicing elit, sed do eiusmod tempor incididunt ut labore et dolore magna aliqua. Ut enim ad minim veniam, quis nostrud exercitation ullamco laboris nisi ut aliquip ex ea commodo consequat. Duis aute irure dolor in reprehenderit in voluptate velit esse cillum dolore eu fugiat nulla pariatur. Excepteur sint occaecat cupidatat non proident, sunt in culpa qui officia deserunt mollit anim id est laborum.</p>
        <p class="closing">Thank you</p>
        <div class="signature">Your Name</div>
      </div>
    </section>
  </article>
</body>
</html>
```